Roll label Flyer design

I need a flyer for a roll label printer
Pictures for the project are located here:
https://brindlework.filedrop.example/d-k7mx2291q0a553714

Text I want is located here:
https://brindlework.example/roll-labels.php

Target Market(s)

Manufactures, wholesalers

Industry/Entity Type

Printing

Requirements
Must have
• Lots of pictures. Our phone number 800-472-6018. Website www.brindlework.example

```html
<!DOCTYPE html>
<html lang="en">
<head>
<meta charset="utf-8">
<title>Brindlework Roll Label Flyer</title>
<link rel="stylesheet" href="https://fonts.googleapis.com/css2?family=Bebas+Neue&family=Oswald:wght@600&family=Open+Sans:wght@400&display=swap">
<style>
  :root {
    --brand-red: #c01a2b;
    --ink: #1e1e1e;
    --ink-soft: #3a3a3a;
    --swoosh-grey: #a9a9a9;
    --stage: #858585;
    --paper: #ffffff;
  }
  html, body { margin: 0; padding: 0; width: 1200px; height: 1200px; overflow: hidden; background: var(--stage); }
  .flyer {
    position: absolute; left: 190px; top: 25px;
    width: 858px; height: 1202px;
    transform: scale(0.956); transform-origin: 0 0;
    background: var(--paper); overflow: hidden;
    box-shadow: 0 6px 18px rgba(0,0,0,.35);
    font-family: "Open Sans", sans-serif; color: var(--ink);
  }
  .flyer-shapes { position: absolute; inset: 0; }
  .brand { position: absolute; left: 30px; top: 600px; display: flex; align-items: center; gap: 18px; }
  .brand-dot { width: 78px; height: 78px; border-radius: 50%; background: var(--brand-red); }
  .brand-name { font-family: "Oswald", sans-serif; font-weight: 600; font-size: 36px; letter-spacing: 9px; color: var(--ink); }
  .headline { position: absolute; left: 30px; top: 712px; margin: 0; font-family: "Bebas Neue", sans-serif; font-weight: 400; font-size: 92px; line-height: 1; color: var(--brand-red); letter-spacing: -1px; }
  .tagline { position: absolute; left: 30px; top: 793px; margin: 0; font-family: "Bebas Neue", sans-serif; font-size: 29px; color: var(--ink-soft); letter-spacing: 0; }
  .section-title { position: absolute; margin: 0; font-family: "Bebas Neue", sans-serif; font-weight: 400; font-size: 27px; color: var(--brand-red); border-bottom: 3px solid var(--brand-red); padding-bottom: 2px; line-height: 1.1; }
  .title-labels { left: 30px; top: 849px; width: 266px; }
  .title-features { left: 448px; top: 726px; width: 134px; }
  .title-markets { left: 448px; top: 902px; width: 360px; }
  .labels-copy { position: absolute; left: 30px; top: 895px; width: 330px; margin: 0; font-size: 15.5px; line-height: 20px; text-align: justify; }
  .bullet-list { position: absolute; left: 448px; margin: 0; padding: 0; list-style: none; font-size: 15.5px; line-height: 20.2px; }
  .bullet-list li { position: relative; padding-left: 17px; }
  .bullet-list li::before { content: ""; position: absolute; left: 0; top: 7px; width: 7px; height: 7px; border-radius: 50%; background: var(--brand-red); }
  .features-list { top: 761px; }
  .markets-list { top: 940px; }
  .markets-list li { padding-left: 22px; }
  .contact { position: absolute; left: 52px; top: 1070px; margin: 0; padding: 0; list-style: none; color: var(--paper); font-size: 19px; line-height: 34px; }
  .contact li { display: flex; align-items: center; gap: 12px; }
  .contact svg { width: 18px; height: 18px; fill: var(--paper); }
</style>
</head>
<body>
<main class="flyer">
  <svg class="flyer-shapes" viewBox="0 0 858 1202" width="858" height="1202">
    <defs>
      <linearGradient id="plant-floor" x1="0" y1="0" x2="1" y2="1">
        <stop offset="0" stop-color="#d9dde2"/>
        <stop offset=".5" stop-color="#9aa1a8"/>
        <stop offset="1" stop-color="#5b5f63"/>
      </linearGradient>
      <linearGradient id="sheet-stack" x1="0" y1="0" x2="1" y2="0">
        <stop offset="0" stop-color="#6f78b8"/><stop offset=".5" stop-color="#2a2f6a"/><stop offset="1" stop-color="#8a90c4"/>
      </linearGradient>
      <linearGradient id="warning-roll" x1="0" y1="0" x2="1" y2="1">
        <stop offset="0" stop-color="#e04a55"/><stop offset=".6" stop-color="#c4303b"/><stop offset="1" stop-color="#5a5a5a"/>
      </linearGradient>
      <linearGradient id="printed-roll" x1="0" y1="0" x2="1" y2="1">
        <stop offset="0" stop-color="#c8ccd0"/><stop offset=".45" stop-color="#1c1e24"/><stop offset="1" stop-color="#b8b070"/>
      </linearGradient>
    </defs>
    <rect x="0" y="0" width="858" height="700" fill="url(#plant-floor)" role="img" aria-label="Photo of a roll label printing press on the factory floor"/>
    <path d="M0,445 C220,385 520,395 858,600 L858,700 L0,700 Z" fill="var(--swoosh-grey)"/>
    <path d="M0,452 C220,400 520,410 858,615 L858,640 C520,430 220,420 0,470 Z" fill="var(--brand-red)"/>
    <path d="M0,462 C220,418 520,430 858,640 L858,1202 L0,1202 Z" fill="var(--paper)"/>
    <circle cx="292" cy="392" r="93" fill="url(#sheet-stack)" stroke="var(--brand-red)" stroke-width="6" role="img" aria-label="Photo of label sheets stacked in a press"/>
    <circle cx="470" cy="440" r="113" fill="url(#warning-roll)" stroke="var(--brand-red)" stroke-width="6" role="img" aria-label="Photo of a roll of red warning labels"/>
    <circle cx="665" cy="542" r="153" fill="url(#printed-roll)" stroke="var(--brand-red)" stroke-width="6" role="img" aria-label="Photo of a printed black label roll on a spindle"/>
    <path d="M420,1090 C580,1150 720,1130 858,1020 L858,1060 C720,1170 560,1170 420,1100 Z" fill="var(--swoosh-grey)"/>
    <path d="M0,1030 C160,995 300,1020 440,1085 C580,1150 720,1160 858,1070 L858,1202 L0,1202 Z" fill="var(--brand-red)"/>
  </svg>

  <div class="brand">
    <span class="brand-dot"></span>
    <span class="brand-name">BRINDLEWORK</span>
  </div>

  <h1 class="headline">OUTSTANDING</h1>
  <p class="tagline">CUSTOMER SERVICE, COMPETITIVE PRICING</p>

  <h2 class="section-title title-labels">ROLL/PRODUCT LABELS</h2>
  <p class="labels-copy">Long or short run. Digital or flexographic. Standard shapes or unique, custom diecuts. Simple spot colors or full color with every embellishment. Let us help you create the perfect label for your application.</p>

  <h2 class="section-title title-features">FEATURES:</h2>
  <ul class="bullet-list features-list">
    <li>Foil-Stamping</li>
    <li>Embossing</li>
    <li>Spot Varnishes</li>
    <li>Instant Redeemable Coupons</li>
    <li>Expanded Content/Booklet Labels</li>
  </ul>

  <h2 class="section-title title-markets">SPECIALTY MARKETS WE SERVICE INCLUDE:</h2>
  <ul class="bullet-list markets-list">
    <li>Health &amp; Beauty</li>
    <li>Food &amp; Beverage</li>
    <li>Wine &amp; Spirits</li>
    <li>Industrial Safety &amp; Warning</li>
    <li>Promotional</li>
    <li>Compliance (I.E. UL, CSA, California Prop 65)</li>
  </ul>

  <ul class="contact">
    <li><svg viewBox="0 0 24 24"><path d="M6.6 10.8a15 15 0 0 0 6.6 6.6l2.2-2.2a1 1 0 0 1 1-.25 11.4 11.4 0 0 0 3.6.57 1 1 0 0 1 1 1V20a1 1 0 0 1-1 1A17 17 0 0 1 3 4a1 1 0 0 1 1-1h3.5a1 1 0 0 1 1 1c0 1.25.2 2.45.57 3.57a1 1 0 0 1-.25 1z"/></svg>(800) 472-6018</li>
    <li><svg viewBox="0 0 24 24"><path d="M6 2h9v5H6zM4 8h16a2 2 0 0 1 2 2v10a2 2 0 0 1-2 2H4a2 2 0 0 1-2-2V10a2 2 0 0 1 2-2zm2 4v2h3v-2zm5 0v2h3v-2zm-5 4v2h3v-2zm5 0v2h3v-2z"/></svg>(509) 555-0142</li>
    <li><svg viewBox="0 0 24 24"><path d="M12 2a10 10 0 1 0 0 20 10 10 0 0 0 0-20zm6.9 6h-3a15 15 0 0 0-1.3-3.9A8 8 0 0 1 18.9 8zM12 4a13 13 0 0 1 1.9 4h-3.8A13 13 0 0 1 12 4zM4.3 14a8 8 0 0 1 0-4h3.4a16 16 0 0 0 0 4zm.8 2h3a15 15 0 0 0 1.3 3.9A8 8 0 0 1 5.1 16zm3-8h-3a8 8 0 0 1 4.3-3.9A15 15 0 0 0 8.1 8zM12 20a13 13 0 0 1-1.9-4h3.8A13 13 0 0 1 12 20zm2.3-6H9.7a14 14 0 0 1 0-4h4.6a14 14 0 0 1 0 4zm.3 5.9a15 15 0 0 0 1.3-3.9h3a8 8 0 0 1-4.3 3.9zM16.3 14a16 16 0 0 0 0-4h3.4a8 8 0 0 1 0 4z"/></svg>www.brindlework.example</li>
  </ul>
</main>
</body>
</html>
```